Ginger Beer Can Design for a none alcoholic bavarage

We need a cool, modern, fresh design for a can.

- 330ml sleek can size
- 0.0% alcohol
- BIO
- ingredience: Water, Sugar, Ginger, limejuice, Gummi Arabicum, Carbonisation
- Energy table of fats, carbs, protein, etc.
- address: Quiet Meadow Drinks, Lindenweg 42, 4052 Basel

```html
<!DOCTYPE html>
<html lang="en">
<head>
<meta charset="UTF-8">
<title>Ginger Beer – Can Label</title>
<link rel="stylesheet" href="https://fonts.googleapis.com/css2?family=Anton&family=Fjalla+One&family=Montserrat:wght@400;600;700&family=Permanent+Marker&display=swap">
<style>
  :root{
    --stage:#28777a;
    --paper:#f0f0f0;
    --teal-deep:#07595b;
    --teal-ink:#0b5a5a;
    --silver-1:#ffffff;
    --silver-2:#b9bcbe;
    --leaf:#1d9f3c;
    --ginger-1:#d9b27a;
    --ginger-2:#8fb34a;
    --facts-line:#9fcfcf;
    --white-soft:#eaeaea;
  }
  *{margin:0;padding:0;box-sizing:border-box}
  html,body{width:1200px;height:776px;overflow:hidden;background:var(--stage)}
  .canvas{position:relative;width:1200px;height:776px;background:var(--stage)}
  .label{position:absolute;left:284px;top:38px;width:635px;height:703px;background:var(--paper);overflow:hidden}
  .label-wave{position:absolute;inset:0;width:100%;height:100%}

  .title-main{position:absolute;left:82px;top:60px;font-family:"Anton",sans-serif;font-weight:400;color:var(--teal-deep);font-size:96px;line-height:88px;letter-spacing:-1px}
  .title-small{position:absolute;left:393px;top:52px;font-family:"Anton",sans-serif;font-weight:400;color:var(--teal-deep);font-size:44px;line-height:48px}

  .info{position:absolute;left:372px;font-family:"Fjalla One",sans-serif;font-style:italic;color:var(--teal-ink);font-size:16px;line-height:19px;letter-spacing:.6px;transform:skewX(-8deg);transform-origin:left}
  .ingredients{top:152px}
  .address{top:248px}

  .health-drink{position:absolute;left:182px;top:300px;font-family:"Permanent Marker",sans-serif;color:var(--leaf);font-size:24px;transform:rotate(-17deg);transform-origin:left center;white-space:nowrap}
  .bio-badge{position:absolute;left:82px;top:300px;width:72px;height:72px;border-radius:50%;border:4px solid var(--leaf)}

  .ginger-art{position:absolute;border-radius:45% 55% 50% 50%;background:radial-gradient(ellipse at 40% 65%,var(--ginger-1) 0 45%,transparent 70%),radial-gradient(ellipse at 55% 25%,var(--ginger-2) 0 30%,transparent 60%)}
  .ginger-art.top{left:504px;top:290px;width:100px;height:106px}
  .ginger-art.bottom{left:123px;top:434px;width:148px;height:150px}

  .alcohol{position:absolute;left:72px;top:605px;font-family:"Fjalla One",sans-serif;font-style:italic;color:var(--white-soft);font-size:22px;transform:skewX(-8deg)}
  .volume{position:absolute;left:217px;top:592px;font-family:"Anton",sans-serif;color:var(--white-soft);font-size:46px;line-height:54px}

  .facts{position:absolute;left:398px;top:450px;width:182px;height:236px;background:rgba(20,70,72,.55);border:2px solid var(--facts-line);outline:3px solid rgba(20,70,72,.6);padding:4px 7px;font-family:"Montserrat",sans-serif;color:var(--white-soft)}
  .facts-title{font-weight:600;font-size:20px;line-height:22px;color:#dfeeee;white-space:nowrap}
  .facts-meta{font-size:8px;line-height:12.5px}
  .facts-rule{height:4px;background:var(--facts-line);margin:3px 0 4px}
  .facts-head{font-weight:700;font-size:8px;line-height:12px;border-bottom:1px solid var(--facts-line);padding-bottom:1px;margin-bottom:2px}
  .facts-row{display:flex;font-size:8px;line-height:14px;white-space:nowrap}
  .facts-row .dots{flex:1;border-bottom:1px dotted var(--white-soft);margin:0 2px 4px}
  .facts-source{border-top:2px solid var(--facts-line);margin-top:3px;padding-top:3px;font-size:7.5px;line-height:11px;white-space:nowrap}
</style>
</head>
<body>
<main class="canvas">
  <section class="label">
    <svg class="label-wave" viewBox="0 0 1058 1172" preserveAspectRatio="none" aria-hidden="true">
      <defs>
        <linearGradient id="silverBand" x1="0" y1="0" x2="1" y2="0">
          <stop offset="0" stop-color="#ffffff"/>
          <stop offset=".5" stop-color="#b9bcbe"/>
          <stop offset="1" stop-color="#ffffff"/>
        </linearGradient>
      </defs>
      <path d="M90,560 C140,680 260,720 380,650 C460,600 520,560 575,590 C640,555 720,565 800,625 C900,700 980,690 1058,560 L1058,1172 L90,1172 Z" fill="#07595b"/>
      <path d="M90,588 C140,708 260,748 380,678 C460,628 520,588 575,618 C640,583 720,593 800,653 C900,728 980,718 1058,588 L1058,1172 L90,1172 Z" fill="url(#silverBand)"/>
      <path d="M90,615 C140,735 260,775 380,705 C460,655 520,615 575,645 C640,610 720,620 800,680 C900,755 980,745 1058,615 L1058,1172 L90,1172 Z" fill="#07595b"/>
    </svg>

    <h1 class="title-main">Ginger<br>Beer</h1>
    <h2 class="title-small">Ginger Beer</h2>

    <p class="info ingredients">Ingredience:<br>Water, Sugar, Ginger, limejuice,<br>Gummi Arabicum, Carbonisation</p>
    <p class="info address">Quiet Meadow Drinks, Lindenweg 42,<br>4052 Basel</p>

    <div class="bio-badge" aria-label="Organic certification badge"></div>
    <p class="health-drink">HEALTH DRINK</p>

    <div class="ginger-art top" role="img" aria-label="Ginger root with green leaves"></div>
    <div class="ginger-art bottom" role="img" aria-label="Fresh ginger root with green leaves"></div>

    <p class="alcohol">0.0% alcohol</p>
    <p class="volume">330ml</p>

    <div class="facts">
      <div class="facts-title">Serving Facts</div>
      <div class="facts-meta">Serving size<br>Servings per container</div>
      <div class="facts-rule"></div>
      <div class="facts-head">Amount per serving</div>
      <div class="facts-row"><span>Alcohol by volume</span><span class="dots"></span><span>0,0 %</span></div>
      <div class="facts-row"><span>Alcohol per serving (g)</span><span class="dots"></span><span>0</span></div>
      <div class="facts-row"><span>Calories (kcal)</span><span class="dots"></span><span>120-130</span></div>
      <div class="facts-row"><span>Carbohydrates (g)</span><span class="dots"></span><span>3,5-4,5</span></div>
      <div class="facts-row"><span>Fat (g)</span><span class="dots"></span><span>0</span></div>
      <div class="facts-row"><span>Protein (g)</span><span class="dots"></span><span>&lt;1</span></div>
      <div class="facts-row"><span>Sugars (g)</span><span class="dots"></span><span>1-2</span></div>
      <div class="facts-row"><span>Calcium (mg)</span><span class="dots"></span><span>12-13</span></div>
      <div class="facts-row"><span>Potassium (mg)</span><span class="dots"></span><span>100-200</span></div>
      <div class="facts-source">Source: Alpine Nutrition Data Office</div>
    </div>
  </section>
</main>
</body>
</html>
```